Packaging Label Graphic Design

This design is for new packaging that we are about to launch. This label will go around our food container. We are hoping to go with some parts of the label clear (so you can still see the food inside) and the other half colored. We are open to your creativity. I will attached our logo , as that will need to be on there. As well as our website www.harvobrightfare.com, as well as instagram @harvobrightfare. We use the slogan "Elevate Your Life". You can use that too.
Our food is a healthier concept, and our food has a high volume of fresh ingredients. These containers will particularly be used for our Meal Prep(Fully cooked meals that you just need to heat up). The final design should look so goo that you would want to put it on your instagram before eating it :) The colours we currently play around with are navy blue, the grey and green you see in our logo, we also have a mustard colour that we have been implementing. Sizes that it needs to be is attached.

Target Market(s)

Ages 25-35

Requirements
Must have
• Our logo, website, & social media handles, a clear patch (with a design in it) so customers can see the food better. Get Creative.
Nice to have
• Color , stand out to customers, distinguished look.

```html
<!DOCTYPE html>
<html lang="en">
<head>
<meta charset="UTF-8">
<title>Harvo Brightfare – Meal Prep Label</title>
<link href="https://fonts.googleapis.com/css2?family=Montserrat:wght@800&family=Poppins:wght@500&family=Roboto:wght@500&family=Great+Vibes&display=swap" rel="stylesheet">
<style>
  :root{
    --green:#8cbf3f;
    --grey:#8a8c8f;
    --grey-dark:#5f6164;
    --white:#ffffff;
    --backdrop:#e8eaed;
    --clear-top:#c9d0d8;
    --clear-bottom:#d9dee4;
  }
  *{margin:0;padding:0;box-sizing:border-box}
  html,body{width:912px;height:1200px;overflow:hidden;background:var(--backdrop)}
  .canvas{position:relative;width:912px;height:1200px}
  .label{position:absolute;left:76px;width:760px;height:342px;overflow:hidden;border-radius:2px;box-shadow:0 4px 18px rgba(20,30,50,.12);display:flex;flex-direction:column}
  .label--solid{top:196px;background:var(--white)}
  .label--clear{top:662px}
  .label__window{position:absolute;inset:0;background:linear-gradient(180deg,var(--clear-top),var(--clear-bottom))}
  .label__face{position:relative;flex:1;padding:44px 48px 0}
  .label__rule{position:relative;height:6px;background:var(--grey)}
  .label--clear .label__rule{background:var(--white)}
  .label__band{position:relative;height:78px;background:var(--green);display:flex;align-items:center;justify-content:center}
  .brand__name{font-family:"Montserrat",sans-serif;font-weight:800;font-size:40px;letter-spacing:1px;color:var(--grey-dark);line-height:1;text-transform:uppercase}
  .brand__tag{margin-top:12px;font-family:"Roboto",sans-serif;font-weight:500;font-size:22px;color:var(--green);letter-spacing:.3px}
  .brand__tag span{color:var(--grey);padding:0 8px}
  .brand__slogan{margin:10px 0 0 72px;font-family:"Great Vibes",cursive;font-size:34px;line-height:1.2;color:var(--grey)}
  .label--clear .brand__name,
  .label--clear .brand__slogan,
  .label--clear .brand__tag span{color:var(--white)}
  .contact{display:flex;gap:28px;font-family:"Poppins",sans-serif;font-weight:500;font-size:20px;color:var(--white)}
  .contact__item{display:flex;align-items:center;gap:8px}
  .contact__icon{width:22px;height:22px}
</style>
</head>
<body>
<div class="canvas">

  <section class="label label--solid">
    <div class="label__face">
      <div class="brand__name">Harvo Brightfare</div>
      <div class="brand__tag">HEALTHY KITCHEN<span>|</span>MEAL PREP</div>
      <div class="brand__slogan">Elevate Your Life</div>
    </div>
    <div class="label__rule"></div>
    <div class="label__band">
      <div class="contact">
        <div class="contact__item">
          <svg class="contact__icon" viewBox="0 0 24 24" fill="none" stroke="currentColor" stroke-width="1.6"><circle cx="12" cy="12" r="10"/><ellipse cx="12" cy="12" rx="4.5" ry="10"/><path d="M2 12h20M4 7h16M4 17h16"/></svg>
          www.harvobrightfare.com
        </div>
        <div class="contact__item">
          <svg class="contact__icon" viewBox="0 0 24 24"><circle cx="12" cy="12" r="10" fill="none" stroke="currentColor" stroke-width="2"/></svg>
          @harvobrightfare
        </div>
      </div>
    </div>
  </section>

  <section class="label label--clear">
    <div class="label__window" role="img" aria-label="Clear window showing the meal inside: grilled chicken, rice, egg and vegetables"></div>
    <div class="label__face">
      <div class="brand__name">Harvo Brightfare</div>
      <div class="brand__tag">HEALTHY KITCHEN<span>|</span>MEAL PREP</div>
      <div class="brand__slogan">Elevate Your Life</div>
    </div>
    <div class="label__rule"></div>
    <div class="label__band">
      <div class="contact">
        <div class="contact__item">
          <svg class="contact__icon" viewBox="0 0 24 24" fill="none" stroke="currentColor" stroke-width="1.6"><circle cx="12" cy="12" r="10"/><ellipse cx="12" cy="12" rx="4.5" ry="10"/><path d="M2 12h20M4 7h16M4 17h16"/></svg>
          www.harvobrightfare.com
        </div>
        <div class="contact__item">
          <svg class="contact__icon" viewBox="0 0 24 24"><circle cx="12" cy="12" r="10" fill="none" stroke="currentColor" stroke-width="2"/></svg>
          @harvobrightfare
        </div>
      </div>
    </div>
  </section>

</div>
</body>
</html>
```